Email Banner (LumenBriefs)

We require an email banner for our email promotions sent to prospect clients. The banner needs to contain the wording LumenBriefs and use the same colour scheme as the logos attached.

This is for B2B professional's so needs to look like a place you would come to read technology articles.

```html
<!DOCTYPE html>
<html lang="en">
<head>
<meta charset="utf-8">
<title>LumenBriefs Email Banner</title>
<link href="https://fonts.googleapis.com/css2?family=Outfit:wght@300;600&display=swap" rel="stylesheet">
<style>
  :root {
    --stage-dark: #000000;
    --stage-light: #ffffff;
    --band-green: #4a9a26;
    --band-mid-green: #4aa35a;
    --band-teal: #2a9fa2;
    --band-blue: #0d74c9;
    --headline: #ffffff;
    --tag-ink: #0f2236;
  }
  * { margin: 0; padding: 0; box-sizing: border-box; }
  html, body {
    width: 1200px;
    height: 1200px;
    overflow: hidden;
  }
  body {
    font-family: "Outfit", sans-serif;
    position: relative;
  }
  .stage {
    position: absolute;
    left: 0;
    width: 1200px;
    height: 600px;
  }
  .stage--dark { top: 0; background: var(--stage-dark); }
  .stage--light { top: 600px; background: var(--stage-light); }

  .banner {
    position: absolute;
    left: 207px;
    top: 223px;
    width: 787px;
    height: 153px;
    overflow: hidden;
  }
  .banner__backdrop {
    position: absolute;
    inset: 0;
    background: linear-gradient(90deg,
      var(--band-green) 0%,
      var(--band-mid-green) 35%,
      var(--band-teal) 65%,
      var(--band-blue) 100%);
  }
  .banner__wordmark {
    position: absolute;
    top: 38px;
    font-size: 84px;
    line-height: 1;
    color: var(--headline);
    letter-spacing: -0.5px;
    white-space: nowrap;
  }
  .banner--centered .banner__wordmark { left: 140px; }
  .banner--tagged .banner__wordmark { left: 81px; }
  .wordmark__bold { font-weight: 600; }
  .wordmark__light { font-weight: 300; letter-spacing: 1px; }

  .banner__site {
    position: absolute;
    top: 7px;
    right: 7px;
    display: flex;
    align-items: center;
    gap: 5px;
    font-size: 18px;
    font-weight: 600;
    color: var(--tag-ink);
  }
  .banner__site-dot {
    width: 10px;
    height: 10px;
    background: var(--tag-ink);
  }
</style>
</head>
<body>
  <section class="stage stage--dark">
    <div class="banner banner--centered">
      <div class="banner__backdrop" role="img" aria-label="Green to blue gradient with a faint circuit board pattern"></div>
      <h1 class="banner__wordmark"><span class="wordmark__bold">Lumen</span><span class="wordmark__light">Briefs</span></h1>
    </div>
  </section>

  <section class="stage stage--light">
    <div class="banner banner--tagged">
      <div class="banner__backdrop" role="img" aria-label="Green to blue gradient with a faint circuit board pattern"></div>
      <div class="banner__site"><span class="banner__site-dot"></span><span>LumenBriefs.io</span></div>
      <h1 class="banner__wordmark"><span class="wordmark__bold">Lumen</span><span class="wordmark__light">Briefs</span></h1>
    </div>
  </section>
</body>
</html>
```